BrightLoop (1 page) homepage re-design

Our homepage needs a face-lift! We need our homepage on our website re-designed with a fresh and current look and feel. We have all the details, colour codes and a rough wireframe ready, but need a talented designer to put some personality into our ideas.

What we do: BrightLoop is a digital marketing agency with offices in Australia (Sydney) and South Africa (Cape Town). We specialise in SEO, PPC (otherwise known as Zentro PayLine or SEM), content marketing and Zentro Tallyboard. We use these tools to help our clients realise their business dreams.

VISUAL

Style / theme of the design:
Clean, simplistic, fun, flow.

Websites we draw inspiration from:
This is the theme we want to use to build the website
http://demo.vormalayouts.example/vl/?theme=Pebbled
Inspiration:
https://www.ondrapromo.example/
https://www.nelvagrowth.example.au/
https://quimbel.example.au/
https://torvin.layout-works.example/forum/

What we like about the site:
Clean, simple design, good use of white space. The subtle changing background colours, strong contrast with text. Not too busy or distracting.

What we don’t want: Too many different colours.

Target Market(s)

Our target audience: Marketing Managers of small to medium size businesses in Australia.

Industry/Entity Type

Marketing

Number of Pages Required

1 page

Font styles to use
Sans Serif

Requirements
Must have
• Elements to be added on homepage in order and as seen in attachments:
• - Section 1: Video with team as image and a play button add the heading: We help smart marketing managers achieve their KPIs [line break] and reduce their digital marketing overwhelm.
• - Section 2: Solutions section with the 6 solutions displayed in a row.
• - Section 3: Register Free Webinar with video
• - Section 4: Please add 3 case studies (as seen in attached docs there is only 1 but please add 3 below each other)
• - Section 5: Clients. Please add all client logo’s (black and white)
• - Section 6: Our Blog (as seen attached)
• - Section 7: Conferences Attended (please add the title and a paragraph of lorem Ipsom below) and then please add all conference logo’s attached below.
• - Section 8: In The Media (please add all logo’s titled media) white background
• - Section 9: Footer (dark grey footer) add our Zentro honoured affiliate logo here please
• - Section10: Footer - include:
• - Social logos (WorkMesh, Blipster, Pallwall, ReelDrop, Zentro Hub)
• - Navigation
• - Contact details (name, address, phone number, email)
• Colour codes:
• We want to use light greys, white and charcoal grey for the backgrounds with a pop of our green colour to bring out our branding and all CTA’s to be orange, colour codes below:
• Light grey: #F2F2F2
• Charcoal grey: #161616
• Green: #428E29
• CTA’s: #de7532
• PLEASE NOTE: Please see attached pdf titled: homepagecopybrief.pdf for all the titles and statistics that need to go on the homepage
Should not have
• Too much colour, icons should not be different colours

```html
<!DOCTYPE html>
<html lang="en">
<head>
<meta charset="utf-8">
<title>BrightLoop – Digital Marketing Agency</title>
<link href="https://fonts.googleapis.com/css2?family=Lato:wght@400;700;900&family=Open+Sans:wght@400;600;700&display=swap" rel="stylesheet">
<style>
:root{
  --green:#428E29;
  --orange:#de7532;
  --light:#F2F2F2;
  --charcoal:#161616;
  --footer:#2a2a2a;
  --text:#333;
  --muted:#777;
  --line:#e1e1e1;
  --white:#fff;
  --mark:#555;
}
*{box-sizing:border-box;margin:0;padding:0}
html,body{width:1200px;height:3748px;overflow:hidden}
body{font-family:"Open Sans",Arial,sans-serif;color:var(--text);background:var(--white);font-size:13px;line-height:1.6}
h1,h2,h3,h4{font-family:"Lato",Arial,sans-serif}
.wrap{width:1000px;margin:0 auto;position:relative}
.btn{display:inline-block;background:var(--orange);color:var(--white);font:700 10px "Lato",sans-serif;letter-spacing:.5px;padding:7px 16px;border-radius:2px;text-transform:uppercase}
.section-title{text-align:center;font-size:26px;font-weight:900;color:var(--charcoal);letter-spacing:.5px}

/* hero */
.hero{height:560px;position:relative;overflow:hidden}
.hero-photo{position:absolute;inset:0;background:linear-gradient(180deg,#5b5550 0%,#3f3a36 45%,#2b2724 100%)}
.hero-shade{position:absolute;inset:0;background:radial-gradient(ellipse at 50% 45%,rgba(255,255,255,.08),rgba(0,0,0,.35))}
.topbar{position:absolute;top:0;left:0;right:0;height:78px}
.brand{position:absolute;left:100px;top:18px;display:flex;align-items:center;gap:8px;font:900 20px "Lato",sans-serif;color:var(--white)}
.brand i{width:16px;height:16px;background:var(--green);display:block}
.contact-strip{position:absolute;right:100px;top:10px;display:flex;gap:26px;color:#ddd;font-size:10px}
.nav{position:absolute;right:100px;top:40px;display:flex;background:rgba(0,0,0,.45)}
.nav a{color:var(--white);font:600 10px "Open Sans",sans-serif;padding:8px 15px;text-decoration:none}
.nav a.active{background:var(--green)}
.hero-copy{position:absolute;top:268px;left:0;right:0;text-align:center;color:var(--white)}
.hero-copy h1{font-size:40px;font-weight:900;line-height:1.15;text-shadow:0 2px 6px rgba(0,0,0,.4)}
.hero-copy p{font-size:17px;margin:6px 0 20px}
.hero-copy .btn{font-size:12px;padding:10px 22px}

/* solutions */
.solutions{height:590px;background:var(--white);padding-top:40px}
.solution-grid{display:grid;grid-template-columns:repeat(3,1fr);gap:36px 30px;margin-top:36px}
.solution-card{background:var(--light);border-bottom:4px solid var(--green);height:196px;padding:24px 22px}
.solution-card h3{font-size:13px;font-weight:900;color:var(--charcoal);margin-bottom:10px}
.solution-card p{font-size:11px;color:var(--muted);line-height:1.55;margin-bottom:14px}

/* webinar */
.webinar{height:350px;background:var(--light);padding-top:70px}
.webinar .wrap{display:flex;gap:40px}
.webinar-video{width:440px;height:220px;background:linear-gradient(135deg,#4a4d52,#23252a);position:relative}
.webinar-video svg{position:absolute;left:50%;top:50%;transform:translate(-50%,-50%)}
.webinar-copy{flex:1;padding-top:4px}
.webinar-copy h4{font-size:18px;font-weight:700;color:var(--charcoal);letter-spacing:.5px}
.webinar-copy h2{font-size:40px;font-weight:900;color:var(--charcoal);line-height:1;margin-bottom:12px}
.webinar-copy p{font-size:11px;color:var(--muted);margin-bottom:14px}
.webinar-input{width:420px;height:28px;border:1px solid #ccc;background:var(--white);font-size:10px;color:#aaa;padding:6px 10px;margin-bottom:10px}

/* case studies */
.cases{height:650px;padding-top:40px}
.cases .wrap{display:flex;gap:40px;margin-top:36px}
.case-list{width:260px}
.case{margin-bottom:38px}
.case-head{display:flex;align-items:center;gap:12px}
.case-head h4{font-size:11px;font-weight:900;color:var(--charcoal)}
.case-mark{display:flex;align-items:center;gap:5px;font:700 10px "Open Sans",sans-serif;color:var(--charcoal)}
.case-mark i{width:10px;height:10px;background:var(--charcoal);display:block}
.case p{font-size:10px;color:var(--muted);margin:6px 0 2px}
.case strong{font:900 48px/1 "Lato",sans-serif;color:var(--charcoal)}
.chart-panel{flex:1;background:var(--light);height:480px;padding:30px}

/* partner names (set as plain text) */
.name-mark{font:700 16px "Lato",sans-serif;color:var(--mark);display:flex;align-items:center;gap:8px;white-space:nowrap}
.name-mark i{width:12px;height:12px;background:var(--mark);display:block}

/* clients */
.clients{height:240px;padding-top:40px;text-align:center}
.clients .sub{font-size:11px;color:var(--muted);margin-top:4px}
.logo-row{display:flex;justify-content:space-between;align-items:center;margin-top:44px}

/* blog */
.blog{height:370px;background:var(--light);padding-top:34px}
.blog-grid{display:flex;gap:30px;margin-top:28px}
.blog-card{flex:1;height:226px;position:relative;padding:150px 24px 0}
.blog-card.business{background:linear-gradient(135deg,#5d6a5f,#2f3a33)}
.blog-card.culture{background:linear-gradient(160deg,#6f7d8c,#384452)}
.blog-card h3{color:var(--white);font-size:22px;font-weight:900;margin-bottom:8px}

/* conferences */
.conferences{height:330px;padding-top:40px;text-align:center}
.conferences .lead{font-size:12px;font-weight:700;color:var(--charcoal);margin-top:10px}
.conferences p.body{font-size:11px;color:var(--muted);width:760px;margin:4px auto 0}
.conf-row{display:flex;justify-content:space-between;align-items:center;margin-top:56px}

/* media */
.media{height:330px;border-top:1px solid var(--line);padding-top:40px}
.media .wrap{display:flex;gap:50px}
.media-copy{flex:1}
.media-copy h2{font-size:28px;font-weight:900;color:var(--charcoal)}
.media-copy p{font-size:11px;color:var(--muted);margin:10px 0 40px}
.media-logos{display:flex;gap:30px;align-items:center}
.media-logos .name-mark{font-size:14px;color:var(--text)}
.media-photo{width:460px;height:230px;background:linear-gradient(135deg,#b9b2a8,#6c6259)}

/* footer */
.footer{height:280px;background:var(--footer);color:#bbb;padding-top:44px}
.footer .wrap{display:flex;gap:60px}
.footer-contact{width:280px;font-size:11px}
.footer-contact li{list-style:none;display:flex;gap:10px;margin-bottom:10px;align-items:flex-start}
.socials{display:flex;gap:10px;margin-top:18px;flex-wrap:wrap;width:290px}
.social{display:flex;align-items:center;gap:5px;font-size:10px;color:#ccc}
.social i{width:18px;height:18px;border-radius:50%;background:var(--green);display:block}
.footer-form{width:380px}
.footer-form h4{color:var(--white);font-size:13px;font-weight:700;margin-bottom:12px}
.form-row{display:flex;gap:10px;margin-bottom:10px}
.field{flex:1;height:24px;background:#3a3a3a;font-size:10px;color:#999;padding:4px 8px}
.field.tall{height:48px}
.footer-form .btn{float:right}
.partner{margin-left:auto;width:150px;height:90px;background:var(--white);border-radius:3px;margin-top:20px}
.bottombar{height:48px;background:var(--charcoal);color:#888;font-size:10px}
.bottombar .wrap{display:flex;justify-content:space-between;align-items:center;height:48px}
.bottombar nav{display:flex;gap:18px}
</style>
</head>
<body>

<header class="hero">
  <div class="hero-photo" role="img" aria-label="Photo of the BrightLoop team standing together in the office, with a play button to watch the team video"></div>
  <div class="hero-shade"></div>
  <div class="topbar">
    <div class="brand"><i></i>BrightLoop</div>
    <div class="contact-strip"><span>12 Harbourline Rd, Sydney NSW 2000</span><span>(02) 8000 1234</span></div>
    <nav class="nav">
      <a class="active">Home</a><a>Solutions</a><a>Registration</a><a>Our Blog</a><a>Conferences</a><a>Media</a><a>Contact Us</a>
    </nav>
  </div>
  <div class="hero-copy">
    <h1>We help smart marketing<br>managers achieve their KPIs</h1>
    <p>and reduce their digital marketing overwhelm</p>
    <span class="btn">Get Started &#9656;</span>
  </div>
</header>

<section class="solutions">
  <div class="wrap">
    <h2 class="section-title">SOLUTIONS</h2>
    <div class="solution-grid">
      <article class="solution-card"><h3>GROW REVENUE</h3><p>Turn more clicks into paying customers with campaigns built around the goals your business actually tracks.</p><span class="btn">Read More</span></article>
      <article class="solution-card"><h3>CONVERT LEADS</h3><p>Capture interest early and guide each prospect toward a clear next step with landing pages that work.</p><span class="btn">Read More</span></article>
      <article class="solution-card"><h3>INCREASE BRAND AWARENESS</h3><p>Put your name in front of the right people through search, social and content that feels genuine.</p><span class="btn">Read More</span></article>
      <article class="solution-card"><h3>DATA / KPI'S</h3><p>Clear monthly reports show what moved, what stalled and where the next dollar should be spent wisely.</p><span class="btn">Read More</span></article>
      <article class="solution-card"><h3>INCREASE ENGAGEMENT</h3><p>Keep your audience talking with useful posts, timely emails and offers that invite them to respond quickly.</p><span class="btn">Read More</span></article>
      <article class="solution-card"><h3>MARKETING STRATEGY BUDGETING</h3><p>Map a realistic plan and budget so every channel has a purpose and a measurable target to hit.</p><span class="btn">Read More</span></article>
    </div>
  </div>
</section>

<section class="webinar">
  <div class="wrap">
    <div class="webinar-video" role="img" aria-label="Webinar video still of a person working on a laptop">
      <svg width="56" height="56" viewBox="0 0 56 56"><circle cx="28" cy="28" r="27" fill="rgba(0,0,0,.45)" stroke="#fff" stroke-width="2"/><path d="M22 17 L40 28 L22 39 Z" fill="#fff"/></svg>
    </div>
    <div class="webinar-copy">
      <h4>REGISTER FOR YOUR FREE</h4>
      <h2>WEBINAR</h2>
      <p>Join our free live session and learn how small teams plan smarter campaigns, read their data with confidence and cut wasted spend. We share the exact checklists we use with clients every week, then answer your questions live.</p>
      <div class="webinar-input">Enter your email</div>
      <span class="btn">Submit</span>
    </div>
  </div>
</section>

<section class="cases">
  <h2 class="section-title">CASE STUDIES</h2>
  <div class="wrap">
    <div class="case-list">
      <div class="case"><div class="case-head"><h4>MARROW SELF STORAGE</h4><span class="case-mark"><i></i>Marrow</span></div><p>Organic enquiries grew fivefold within twelve months.</p><strong>500%</strong></div>
      <div class="case"><div class="case-head"><h4>HOMESCOUT</h4><span class="case-mark"><i></i>HomeScout</span></div><p>Leads from search more than doubled this year.</p><strong>123%</strong></div>
      <div class="case"><div class="case-head"><h4>CORVO FITNESS COLLEGE</h4><span class="case-mark"><i></i>Corvo</span></div><p>Bookings rose steadily after the site rebuild.</p><strong>123%</strong></div>
    </div>
    <div class="chart-panel">
      <svg width="580" height="420" viewBox="0 0 580 420" font-family="Open Sans, sans-serif" font-size="10" fill="#888">
        <g stroke="#ddd" stroke-dasharray="3 3">
          <line x1="20" y1="60" x2="560" y2="60"/><line x1="20" y1="140" x2="560" y2="140"/>
          <line x1="20" y1="220" x2="560" y2="220"/><line x1="20" y1="300" x2="560" y2="300"/>
          <line x1="20" y1="360" x2="560" y2="360"/>
        </g>
        <polyline points="40,300 120,296 200,290 280,270 360,220 440,208 520,196" fill="none" stroke="#bbb" stroke-width="2"/>
        <g fill="#fff" stroke="#aaa" stroke-width="2">
          <circle cx="40" cy="300" r="5"/><circle cx="120" cy="296" r="5"/><circle cx="200" cy="290" r="5"/><circle cx="280" cy="270" r="5"/><circle cx="440" cy="208" r="5"/><circle cx="520" cy="196" r="5"/>
        </g>
        <circle cx="360" cy="220" r="6" fill="#428E29"/>
        <g text-anchor="middle"><text x="40" y="385">SUN</text><text x="120" y="385">MON</text><text x="200" y="385">TUE</text><text x="280" y="385">WED</text><text x="360" y="385">THU</text><text x="440" y="385">FRI</text><text x="520" y="385">SAT</text></g>
      </svg>
    </div>
  </div>
</section>

<section class="clients">
  <h2 class="section-title">Who we've worked with</h2>
  <p class="sub">Brands across Australia and South Africa trust us with their growth.</p>
  <div class="wrap logo-row">
    <span class="name-mark"><i></i>Hallbrook Print</span>
    <span class="name-mark">Orvane Systems</span>
    <span class="name-mark"><i></i>Tidemark Group</span>
    <span class="name-mark">Quillon Trade</span>
    <span class="name-mark">Fernway Studio</span>
  </div>
</section>

<section class="blog">
  <div class="wrap">
    <h2 class="section-title">Our Blog</h2>
    <div class="blog-grid">
      <article class="blog-card business" role="img" aria-label="Business blog photo of a team meeting around a table"><h3>Business Blog</h3><span class="btn">Read More</span></article>
      <article class="blog-card culture" role="img" aria-label="Culture blog photo of glass office towers"><h3>Culture Blog</h3><span class="btn">Read More</span></article>
    </div>
  </div>
</section>

<section class="conferences">
  <h2 class="section-title">Conferences Attended</h2>
  <p class="lead">We learn from the best so our clients get the best results.</p>
  <p class="body">Every year our team attends leading search and marketing events to stay ahead of changes, share ideas with peers and bring fresh thinking back to our clients.</p>
  <div class="wrap conf-row">
    <span class="name-mark"><i></i>LandingLab</span>
    <span class="name-mark">Pixelcon</span>
    <span class="name-mark"><i></i>Webmeet Live</span>
    <span class="name-mark">Rankday</span>
    <span class="name-mark">Adsphere</span>
    <span class="name-mark">Funnel Forum</span>
  </div>
</section>

<section class="media">
  <div class="wrap">
    <div class="media-copy">
      <h2>In The Media</h2>
      <p>Our strategists are regularly asked to share their views on search, advertising and growth. Here are a few of the publications that have featured our work and advice for business owners.</p>
      <div class="media-logos">
        <span class="name-mark">Kettle Weekly</span>
        <span class="name-mark">Coastline Press</span>
        <span class="name-mark">Metro Ledger</span>
        <span class="name-mark">Founders Digest</span>
      </div>
    </div>
    <div class="media-photo" role="img" aria-label="Photo of a marketer reviewing analytics on a laptop"></div>
  </div>
</section>

<footer class="footer">
  <div class="wrap">
    <div class="footer-contact">
      <ul>
        <li><svg width="12" height="14" viewBox="0 0 12 14"><path d="M6 0a5 5 0 0 0-5 5c0 4 5 9 5 9s5-5 5-9a5 5 0 0 0-5-5zm0 7a2 2 0 1 1 0-4 2 2 0 0 1 0 4z" fill="#428E29"/></svg><span>BrightLoop<br>12 Harbourline Rd, Sydney NSW 2000</span></li>
        <li><svg width="12" height="12" viewBox="0 0 12 12"><path d="M2 0h2l1 3-1.5 1a7 7 0 0 0 4 4L8.5 6.5l3 1v2.5A2 2 0 0 1 9.5 12C4 12 0 8 0 2.5A2 2 0 0 1 2 0z" fill="#428E29"/></svg><span>(02) 8000 1234</span></li>
        <li><svg width="13" height="10" viewBox="0 0 13 10"><rect width="13" height="10" fill="#428E29"/><path d="M0 0l6.5 5L13 0" fill="none" stroke="#2a2a2a"/></svg><span>hello@brightloop.example</span></li>
      </ul>
      <div class="socials">
        <span class="social"><i></i>WorkMesh</span><span class="social"><i></i>Blipster</span><span class="social"><i></i>Pallwall</span><span class="social"><i></i>ReelDrop</span><span class="social"><i></i>Zentro Hub</span>
      </div>
    </div>
    <div class="footer-form">
      <h4>Get in Touch</h4>
      <div class="form-row"><div class="field">First Name</div><div class="field">Last Name</div></div>
      <div class="form-row"><div class="field">Email</div><div class="field">Phone</div></div>
      <div class="form-row"><div class="field tall">Comment</div></div>
      <span class="btn">Send</span>
    </div>
    <div class="partner" role="img" aria-label="Zentro honoured affiliate badge"></div>
  </div>
</footer>
<div class="bottombar">
  <div class="wrap">
    <nav><span>Home</span><span>Solutions</span><span>Registration</span><span>Our Blog</span><span>Conferences</span><span>Media</span><span>Contact Us</span></nav>
    <span>© 2024 BrightLoop. All rights reserved.</span>
  </div>
</div>

</body>
</html>
```